Website Design for Architecture Practice

I need a home page and one sidebar/content page for an Architecture practice delivered in PSD.

This archictecture practice specialises in one-off, high end homes and commercial properties (restaurant) heavily influenced by Dorian Vessey Kent, particularly his work on the Tarrowby Museum

I am looking for a home page, and a generic content page where we can outline our services, and showcase our homes.

http://notes.qorvenuni.edu.au/studio/Tarrowby%20Lisdane%202.jpg

Target Market(s)

30-70yr old (typically wealthy) property buyers, developers and investors

Industry/Entity Type

Architecture

Number of Pages Required

2 page

Font styles to use
Serif
Sans Serif

Requirements
Must have
• Home page design
• a Content Page design (ie, top nav with sidebar)
Nice to have
• Use any Dorian Vessey Kent images you can find via google etc as placeholders for our own photography (ie they don't need to be licensed as we will be replacing with our own commissioned photography). Full color preferred but feel free to experiment with treating any images as you see fit.

```html
<!DOCTYPE html>
<html lang="en">
<head>
<meta charset="utf-8">
<title>Architecture — Home</title>
<link href="https://fonts.googleapis.com/css2?family=Open+Sans:wght@400;600;700&display=swap" rel="stylesheet">
<style>
:root{
  --page:#2a2a2a;
  --page-deep:#1d1d1d;
  --band:#222;
  --text:#8c8c8c;
  --text-light:#c9c9c9;
  --heading:#d4d4d4;
  --white:#f4f4f4;
  --teal:#2f9aa3;
  --teal-dark:#1f6f78;
  --navy:#161d2b;
  --button:#4a4a4a;
  --rule:#4a4a4a;
}
*{box-sizing:border-box;margin:0;padding:0}
html,body{width:1200px;height:2200px;overflow:hidden}
body{background:var(--page);font-family:"Open Sans",Arial,sans-serif;color:var(--text);position:relative}
.abs{position:absolute}

/* header / hero */
.hero{left:0;top:0;width:1200px;height:600px;
  background:linear-gradient(180deg,#20303c 0%,#3c4a52 30%,#6a5440 55%,#a7783e 68%,#3a3026 82%,#1c1c1c 100%)}
.hero-shade{left:0;top:500px;width:1200px;height:260px;background:linear-gradient(180deg,rgba(29,29,29,0) 0%,var(--band) 40%,var(--page) 100%)}
.topnav{left:0;top:0;width:1200px;height:64px;background:rgba(10,12,14,.75);border-bottom:1px solid rgba(255,255,255,.08)}
.nav-group{top:22px;display:flex;gap:34px;font-size:14px;font-weight:600;color:var(--text-light)}
.nav-group a{color:inherit;text-decoration:none}
.nav-group a.active{color:var(--white);border-bottom:2px solid var(--teal);padding-bottom:4px}
.brand{left:510px;top:16px;width:180px;text-align:center;font-size:24px;font-weight:700;color:var(--white);letter-spacing:.5px}
.slide-arrow{top:240px;width:36px;height:36px;border-radius:50%;background:rgba(220,220,220,.85)}
.slide-arrow svg{display:block}

.thumb{top:410px;width:200px}
.thumb .pic{height:120px;border:4px solid var(--white);box-shadow:0 6px 14px rgba(0,0,0,.6)}
.thumb .tag{height:28px;margin-top:6px;background:#141414;border:1px solid #555;color:var(--text-light);font-size:11px;font-weight:700;text-transform:uppercase;text-align:center;line-height:26px;letter-spacing:.5px}
.thumb.raised{top:392px}

/* sections */
.rule{left:60px;width:1080px;border-top:1px dashed var(--rule)}
.section-title{left:0;width:1200px;text-align:center;font-size:17px;font-weight:700;color:var(--heading);letter-spacing:1px;text-transform:uppercase}
.copy{font-size:12.5px;line-height:21px;color:var(--text)}
.read-more{display:inline-block;background:var(--button);color:var(--white);font-size:12px;font-weight:600;padding:6px 14px;border-radius:2px}

.framed{border:6px solid var(--white);box-shadow:0 5px 12px rgba(0,0,0,.6)}

.service{top:1240px;width:312px;height:120px;border:3px solid var(--white)}
.service .pic{height:100%}
.service .strip{left:0;bottom:0;width:100%;height:40px;background:rgba(31,111,120,.9);padding:4px 12px}
.service .strip b{display:block;color:#ffd65a;font-size:13px}
.service .strip span{display:block;color:var(--white);font-size:10px}

.project{top:1490px;width:176px;height:190px;background:var(--white);padding:6px}
.project .pic{height:138px}
.project .label{margin-top:6px;height:34px;background:var(--teal);color:var(--white);font-size:14px;font-weight:700;text-align:center;line-height:34px}

.contact-box{left:840px;top:1770px;width:325px;height:315px;background:var(--navy);border:1px solid #3a4458;padding:18px 22px}
.contact-box h3{color:var(--white);font-size:15px;font-weight:700;text-align:center;margin-bottom:14px}
.field{height:26px;background:var(--white);margin-bottom:10px;font-size:11px;color:#777;padding:5px 8px}
.field.tall{height:70px}
.submit{margin:4px auto 0;width:100px;height:28px;background:#0c0f16;color:var(--white);font-size:12px;font-weight:700;text-align:center;line-height:28px;border:1px solid #444}

.footer{left:0;top:2116px;width:1200px;height:84px;background:var(--page-deep);border-top:1px solid #3a3a3a}
.foot-item{top:34px;display:flex;align-items:center;gap:8px;font-size:12px;color:var(--text-light)}
.social{display:flex;gap:6px}
.social span{width:18px;height:18px;background:#3c6fb0;border-radius:2px}
.social span:nth-child(2){background:#3aa3d8}
.social span:nth-child(3){background:#888}
</style>
</head>
<body>

<!-- hero -->
<div class="abs hero" role="img" aria-label="Evening photograph of a modern timber and glass house with lit interiors"></div>
<div class="abs hero-shade"></div>

<header class="abs topnav">
  <nav class="abs nav-group" style="left:200px">
    <a class="active">Home</a><a>About Us</a><a>Services</a>
  </nav>
  <div class="abs brand">Architecture</div>
  <nav class="abs nav-group" style="left:730px">
    <a>Projects</a><a>Awards</a><a>Contact</a>
  </nav>
</header>

<div class="abs slide-arrow" style="left:36px">
  <svg width="36" height="36" viewBox="0 0 36 36"><path d="M21 11 L14 18 L21 25" fill="none" stroke="#333" stroke-width="3"/></svg>
</div>
<div class="abs slide-arrow" style="left:1128px">
  <svg width="36" height="36" viewBox="0 0 36 36"><path d="M15 11 L22 18 L15 25" fill="none" stroke="#333" stroke-width="3"/></svg>
</div>

<div class="abs thumb" style="left:272px">
  <div class="pic" role="img" aria-label="Photograph of a white modern villa" style="background:linear-gradient(180deg,#7fa4c4,#d8d8d2 60%,#6f7d66)"></div>
  <div class="tag">Kelso House</div>
</div>
<div class="abs thumb raised" style="left:496px">
  <div class="pic" role="img" aria-label="Photograph of a glazed pavilion" style="background:linear-gradient(180deg,#5b8fb3,#b9ccd6 55%,#55606a)"></div>
  <div class="tag">Harbour Pavilion</div>
</div>
<div class="abs thumb" style="left:728px">
  <div class="pic" role="img" aria-label="Photograph of a hillside residence" style="background:linear-gradient(180deg,#8fb0c8,#e2ddd0 55%,#6a7258)"></div>
  <div class="tag">Ridge Residence</div>
</div>

<!-- welcome -->
<div class="abs rule" style="top:740px"></div>
<h2 class="abs section-title" style="top:768px">Welcome to Architecture</h2>

<div class="abs framed" role="img" aria-label="Black and white portrait photograph of the architect" style="left:70px;top:818px;width:250px;height:128px;background:linear-gradient(135deg,#d9d9d9,#7a7a7a 55%,#3a3a3a);transform:rotate(-3deg)"></div>
<div class="abs framed" role="img" aria-label="Photograph of the Tarrowby Museum by the river" style="left:70px;top:964px;width:250px;height:110px;background:linear-gradient(180deg,#9bb9d6,#c9c3b6 55%,#5c5d58)"></div>

<p class="abs copy" style="left:360px;top:812px;width:790px">We design one-off homes and considered commercial spaces for clients who value light, material and proportion. Every commission begins with the site: its slope, its views, its weather and its history. From there we shape a building that belongs to its place, drawn by hand before it is modelled, and refined with care until each junction, opening and surface feels inevitable.</p>
<p class="abs copy" style="left:360px;top:900px;width:790px">Our practice follows the organic tradition, treating structure, landscape and interior as one continuous idea. Cantilevered roofs, long horizontal lines and warm natural timber give our houses a calm, grounded presence, while generous glazing opens each room to the garden beyond. We work closely with builders and engineers so the finished home matches the first sketch.</p>
<p class="abs copy" style="left:360px;top:988px;width:790px">For restaurants and commercial clients we bring the same attention to detail, creating sculptural interiors that guests remember long after the meal. Whether you are planning a private residence, a development or an investment property, we would welcome the chance to talk through your ideas.</p>
<div class="abs" style="left:372px;top:1070px"><span class="read-more">Read More</span></div>

<!-- services -->
<div class="abs rule" style="top:1150px"></div>
<h2 class="abs section-title" style="top:1180px">Services</h2>

<div class="abs service" style="left:120px">
  <div class="pic" role="img" aria-label="Photograph of a curved modern roof" style="background:linear-gradient(160deg,#e8eef2,#8fb2c8 50%,#3e6f8a)"></div>
  <div class="abs strip"><b>Service 01</b><span>Residential design and planning</span></div>
</div>
<div class="abs service" style="left:444px">
  <div class="pic" role="img" aria-label="Photograph of a city skyline" style="background:linear-gradient(180deg,#bfd0dc,#d8c7a8 55%,#7a6a58)"></div>
  <div class="abs strip"><b>Service 02</b><span>Commercial and restaurant interiors</span></div>
</div>
<div class="abs service" style="left:768px">
  <div class="pic" role="img" aria-label="Photograph of a design meeting over drawings" style="background:linear-gradient(160deg,#2a3d52,#4f6d8c 50%,#c7c7c2)"></div>
  <div class="abs strip"><b>Service 03</b><span>Interior and landscape concepts</span></div>
</div>

<!-- featured projects -->
<div class="abs rule" style="top:1400px"></div>
<h2 class="abs section-title" style="top:1430px">Featured Projects</h2>

<div class="abs project" style="left:32px"><div class="pic" role="img" aria-label="Photograph of a completed house project" style="background:linear-gradient(180deg,#9fc0d8,#e6e2d8 55%,#6f8060)"></div><div class="label">Project #1</div></div>
<div class="abs project" style="left:224px"><div class="pic" role="img" aria-label="Photograph of a completed house project" style="background:linear-gradient(180deg,#9fc0d8,#e6e2d8 55%,#6f8060)"></div><div class="label">Project #2</div></div>
<div class="abs project" style="left:416px"><div class="pic" role="img" aria-label="Photograph of a completed house project" style="background:linear-gradient(180deg,#9fc0d8,#e6e2d8 55%,#6f8060)"></div><div class="label">Project #3</div></div>
<div class="abs project" style="left:608px"><div class="pic" role="img" aria-label="Photograph of a completed house project" style="background:linear-gradient(180deg,#9fc0d8,#e6e2d8 55%,#6f8060)"></div><div class="label">Project #4</div></div>
<div class="abs project" style="left:800px"><div class="pic" role="img" aria-label="Photograph of a completed house project" style="background:linear-gradient(180deg,#9fc0d8,#e6e2d8 55%,#6f8060)"></div><div class="label">Project #5</div></div>
<div class="abs project" style="left:992px"><div class="pic" role="img" aria-label="Photograph of a completed house project" style="background:linear-gradient(180deg,#9fc0d8,#e6e2d8 55%,#6f8060)"></div><div class="label">Project #6</div></div>

<!-- awards -->
<div class="abs rule" style="top:1725px;width:740px"></div>
<h2 class="abs section-title" style="top:1755px;width:800px">Awards</h2>
<p class="abs copy" style="left:60px;top:1800px;width:740px">Our work has been recognised by regional and national design institutes for its sensitivity to site and its crafted detail. Recent honours include awards for residential architecture, sustainable building and interior design, along with several features in leading architecture journals.</p>
<div class="abs" style="left:60px;top:1912px"><span class="read-more">Read More</span></div>

<form class="abs contact-box">
  <h3>We Would Love to Hear from You.</h3>
  <div class="field">Name</div>
  <div class="field">E-mail</div>
  <div class="field">Phone</div>
  <div class="field tall">Comments</div>
  <div class="submit">SUBMIT</div>
</form>

<!-- footer -->
<footer class="abs footer">
  <div class="abs foot-item" style="left:40px">
    <svg width="16" height="16" viewBox="0 0 16 16"><path d="M4 1h3l1 4-2 1c1 2 2 3 4 4l1-2 4 1v3c0 1-1 2-2 2C6 14 2 10 2 3c0-1 1-2 2-2z" fill="#c9c9c9"/></svg>
    (555) 010-2846
  </div>
  <div class="abs foot-item" style="left:220px">
    <svg width="18" height="14" viewBox="0 0 18 14"><rect x="1" y="1" width="16" height="12" fill="none" stroke="#c9c9c9" stroke-width="1.5"/><path d="M1 1l8 7 8-7" fill="none" stroke="#c9c9c9" stroke-width="1.5"/></svg>
    studio@architecture.example
  </div>
  <div class="abs foot-item" style="left:460px">
    Connect with Us
    <div class="social"><span></span><span></span><span></span></div>
  </div>
  <div class="abs foot-item" style="left:920px;color:var(--text)">© 2012 Architecture. All rights reserved.</div>
</footer>

</body>
</html>
```